Project Manager Business Card for Top Architectural Firm

Update and design a stunning Senior Project Manager Business Card

MARCO T. DRUMMOND II
Senior Project Manager

H A L C Y O N
A R C H I T E C T U R E L L C.
www.HalcyonGrandEstates.example
4127 NW 52nd Ter. Suite 2308
Miami, FL 33148
C: (305) 555-0184
mdrummond.halcyongrandestates@mailbox.example

Looking to have the logo to be UV Spot ink printed and to be prominent.

Target Market(s)

High end real estate architecture construction

Industry/Entity Type

Architect

Contact Information for Business Card

MARCO T. DRUMMOND II
Senior Project Manager

H A L C Y O N
Miami, FL 33148
C: (305) 555-0184

Font styles to use
Sans Serif

Colors

Designer to choose colors to be used in the design.

Requirements
Must have
• Prominent Logo

```html
<!DOCTYPE html>
<html lang="en">
<head>
<meta charset="utf-8">
<title>Halcyon Architecture – Business Card</title>
<link href="https://fonts.googleapis.com/css2?family=Montserrat:wght@300;400;700&display=swap" rel="stylesheet">
<style>
  :root {
    --page-bg: #e8e5e0;
    --card-dark: #2f2f31;
    --card-light: #ffffff;
    --ink: #1d1d1f;
    --ink-soft: #3a3a3c;
    --brand-blue: #43739e;
    --brand-blue-light: #5f8fc4;
    --brand-orange: #e08a45;
    --logo-grey: #1f1f21;
    --logo-grey-on-dark: #55595e;
  }
  * { box-sizing: border-box; margin: 0; padding: 0; }
  html, body {
    width: 1200px; height: 800px; overflow: hidden;
    background: var(--page-bg);
    font-family: "Montserrat", Arial, sans-serif;
  }
  .sheet {
    width: 1200px; height: 800px;
    display: flex; align-items: center; justify-content: center; gap: 50px;
  }
  .card {
    position: relative;
    width: 540px; height: 310px;
    border-radius: 16px;
    overflow: hidden;
  }

  /* front */
  .card--front { background: var(--card-dark); }
  .front-brand {
    position: absolute; left: 0; right: 0; top: 92px;
    display: flex; align-items: center; justify-content: center; gap: 16px;
  }
  .brand-dot {
    width: 44px; height: 44px; border-radius: 50%;
    background: var(--brand-blue);
  }
  .brand-name {
    font-weight: 400; line-height: 1;
    white-space: nowrap;
  }
  .brand-name__main { display: block; font-size: 34px; letter-spacing: 2px; }
  .brand-name__sub { display: block; font-size: 9px; letter-spacing: 1px; margin-top: 6px; }
  .card--front .brand-name { color: var(--logo-grey-on-dark); }
  .front-url {
    position: absolute; left: 0; right: 0; bottom: 62px;
    text-align: center;
    font-size: 14px; letter-spacing: 2.5px;
    color: var(--brand-blue);
  }

  /* back */
  .card--back { background: var(--card-light); }
  .back-brand {
    position: absolute; right: 34px; top: 30px;
    display: flex; align-items: center; gap: 10px;
  }
  .back-brand .brand-dot { width: 30px; height: 30px; }
  .back-brand .brand-name { color: var(--logo-grey); }
  .back-brand .brand-name__main { font-size: 24px; }
  .back-brand .brand-name__sub { font-size: 7px; margin-top: 4px; }

  .holder { position: absolute; left: 40px; top: 104px; }
  .holder__name {
    font-weight: 700; font-size: 22px; letter-spacing: 0.2px; color: var(--ink);
  }
  .holder__title {
    font-weight: 300; font-size: 14px; letter-spacing: 0.5px;
    color: var(--brand-blue-light); margin-top: 2px;
  }
  .holder__rule {
    width: 46px; height: 2px; background: var(--brand-orange); margin-top: 8px;
  }
  .accent-line {
    position: absolute; left: 0; top: 128px; width: 30px; height: 1.5px;
    background: var(--brand-orange);
  }

  .contacts {
    position: absolute; left: 40px; top: 184px;
    list-style: none;
    display: flex; flex-direction: column; gap: 7px;
  }
  .contacts__item {
    display: flex; align-items: center; gap: 10px;
    font-size: 12px; color: var(--ink-soft);
  }
  .contacts__icon {
    width: 16px; height: 16px; border-radius: 3px;
    background: var(--brand-orange);
    display: flex; align-items: center; justify-content: center;
  }
  .contacts__icon svg { width: 10px; height: 10px; }

  .address-band {
    position: absolute; left: 0; right: 0; bottom: 0; height: 34px;
    display: flex;
  }
  .address-band__pin {
    width: 56px; background: var(--brand-orange);
    display: flex; align-items: center; justify-content: center;
  }
  .address-band__text {
    flex: 1; background: var(--brand-blue);
    color: #fff; font-size: 12.5px; letter-spacing: 0.3px;
    display: flex; align-items: center; padding-left: 16px;
  }
</style>
</head>
<body>
<main class="sheet">

  <section class="card card--front" aria-label="Card front">
    <div class="front-brand">
      <span class="brand-dot"></span>
      <span class="brand-name">
        <span class="brand-name__main">H A L C Y O N</span>
        <span class="brand-name__sub">A R C H I T E C T U R E L L C.</span>
      </span>
    </div>
    <p class="front-url">www.HalcyonGrandEstates.example</p>
  </section>

  <section class="card card--back" aria-label="Card back">
    <div class="back-brand">
      <span class="brand-dot"></span>
      <span class="brand-name">
        <span class="brand-name__main">H A L C Y O N</span>
        <span class="brand-name__sub">A R C H I T E C T U R E L L C.</span>
      </span>
    </div>

    <span class="accent-line"></span>
    <div class="holder">
      <h1 class="holder__name">MARCO T. DRUMMOND II</h1>
      <p class="holder__title">SENIOR PROJECT MANAGER</p>
      <div class="holder__rule"></div>
    </div>

    <ul class="contacts">
      <li class="contacts__item">
        <span class="contacts__icon">
          <svg viewBox="0 0 10 10"><path d="M2 1h2l1 2-1 1a5 5 0 0 0 2 2l1-1 2 1v2c0 .6-.4 1-1 1A8 8 0 0 1 1 2c0-.6.4-1 1-1z" fill="#fff"/></svg>
        </span>
        (305) 555-0184
      </li>
      <li class="contacts__item">
        <span class="contacts__icon">
          <svg viewBox="0 0 10 10" fill="none" stroke="#fff" stroke-width="1"><circle cx="5" cy="5" r="4"/><ellipse cx="5" cy="5" rx="1.8" ry="4"/><path d="M1 5h8"/></svg>
        </span>
        www.HalcyonGrandEstates.example
      </li>
      <li class="contacts__item">
        <span class="contacts__icon">
          <svg viewBox="0 0 10 10" fill="none" stroke="#fff" stroke-width="1"><rect x="1" y="2.5" width="8" height="5.5"/><path d="M1 2.5l4 3 4-3"/></svg>
        </span>
        mdrummond.halcyongrandestates@mailbox.example
      </li>
    </ul>

    <div class="address-band">
      <span class="address-band__pin">
        <svg width="12" height="16" viewBox="0 0 12 16"><path d="M6 0a6 6 0 0 1 6 6c0 4-6 10-6 10S0 10 0 6a6 6 0 0 1 6-6z" fill="#1d1d1f"/><circle cx="6" cy="6" r="2.2" fill="#e08a45"/></svg>
      </span>
      <p class="address-band__text">4127 NW 52nd Ter. Suite 2308 Miami, FL 33148</p>
    </div>
  </section>

</main>
</body>
</html>
```